Washbag retail Packaging

We need a cardboard insert card design for a delicates washbag. The size for front panel would be 9cm wide and height 12cm, then a fold and the back panel would be the same size. This insert is packed into a clear hangsell polybag , and the white mesh washbag is folded up inside. We want to extend our brand using similar fonts , and colours - as shown in the photgraph, the PMS 241 is really our brand colour. But also introduce something appealing a beautiful about the washbag packaging. The washbag itself is a very plain and boring product. I have included an old artwork for the same product - the yellow box which does not suit the range at all. Please note the new packaging is not a box, but an insert card in a poly bag, and there will not be a window.
Updates

Project Deadline Extended Reason: We have extended the deadline to allow more designers to participate and as its our first time using the service. Added Thursday, January 12, 2017

Target Market(s)

Mainly women all ages, Mid range supermarket, lingerie stores, hosiery and stockings stores

Industry/Entity Type

Retail

Font styles to use
Sans Serif

Colors
e667a6
faeaf3
eea4c8
b868aa

Requirements
Must have
• PMS 241 and work with other products in the range
Nice to have
• Something a little more pretty

```html
<!DOCTYPE html>
<html lang="en">
<head>
<meta charset="utf-8">
<title>Wash Bag – Insert Card</title>
<link href="https://fonts.googleapis.com/css2?family=Open+Sans:ital,wght@0,400;0,600;0,700;1,700&family=Yellowtail&display=swap" rel="stylesheet">
<style>
  :root{
    --bg:#dcdcdc;
    --panel:#faeaf3;
    --brand-pink:#e667a6;
    --soft-pink:#eea4c8;
    --violet:#b868aa;
    --cyan:#3ecbe8;
    --ink:#3a3a3a;
    --label:#4a4a4a;
    --navy:#2a2f7a;
  }
  *{margin:0;padding:0;box-sizing:border-box}
  html,body{width:1200px;height:857px;overflow:hidden;background:var(--bg)}
  body{position:relative;font-family:"Open Sans",Arial,sans-serif}
  .side-label{position:absolute;top:32px;font-weight:700;font-size:33px;color:var(--label);letter-spacing:.5px;text-align:center;width:300px}
  .side-label--front{left:122px}
  .side-label--back{left:740px}

  .panel{position:absolute;top:80px;width:572px;height:762px;background:var(--panel);overflow:hidden}
  .panel--front{left:18px}
  .panel--back{left:608px}

  .colour-field{position:absolute;top:32px;width:492px;height:696px;background:var(--brand-pink);
    border-radius:14px;box-shadow:0 0 14px 6px var(--brand-pink)}
  .panel--front .colour-field{left:42px}
  .panel--back .colour-field{left:48px}

  .heart-art{position:absolute;left:60px;top:150px;width:460px;height:560px;border-radius:50%;
    background:radial-gradient(ellipse at center,rgba(255,255,255,.14),rgba(255,255,255,0) 70%)}
  .flower{position:absolute;width:70px;height:70px;border-radius:50%;
    background:radial-gradient(circle,var(--panel) 10%,var(--violet) 18%,var(--soft-pink) 60%,rgba(238,164,200,0) 72%)}

  .brand{position:absolute;left:186px;top:36px;width:236px;height:62px;display:flex;align-items:center;justify-content:center;gap:10px}
  .brand-mark{width:14px;height:14px;border-radius:50%;background:var(--navy)}
  .brand-name{font-weight:700;font-size:34px;color:var(--navy)}

  .title{position:absolute;color:var(--cyan);font-weight:600;letter-spacing:-1px;
    text-shadow:-2px 0 #fff,0 2px #fff,2px 0 #fff,0 -2px #fff,3px 4px 8px rgba(80,30,60,.45)}
  .panel--front .title{left:94px;top:214px;font-size:90px;line-height:1}
  .subtitle{position:absolute;left:254px;top:394px;font-size:40px;font-weight:600;color:var(--cyan);
    text-shadow:-1px 0 #fff,0 1px #fff,1px 0 #fff,0 -1px #fff,2px 3px 6px rgba(80,30,60,.4)}
  .tagline{position:absolute;left:40px;top:460px;width:490px;text-align:center;font-family:"Yellowtail",cursive;
    font-size:50px;line-height:68px;color:var(--ink);
    text-shadow:0 0 4px #fff,0 0 8px #fff,0 0 12px rgba(255,255,255,.8)}

  .panel--back .title{left:0;width:572px;text-align:center;top:74px;font-size:64px;line-height:1}
  .copy{position:absolute;left:48px;top:188px;width:492px;text-align:center;font-size:15.5px;line-height:21.5px;
    color:var(--ink);letter-spacing:-.3px;text-shadow:0 0 3px #fff,0 0 6px #fff}
  .copy h3{font-size:17px;font-style:italic;font-weight:700;line-height:24px}
  .copy .spec{margin-top:19px;font-size:14px;line-height:19px}
</style>
</head>
<body>
  <div class="side-label side-label--front">FRONT</div>
  <div class="side-label side-label--back">BACK</div>

  <section class="panel panel--front">
    <div class="colour-field"></div>
    <div class="heart-art" role="img" aria-label="Sketched white heart outlines"></div>
    <div class="flower" role="img" aria-label="Violet flower" style="left:10px;top:10px"></div>
    <div class="flower" role="img" aria-label="Violet flower" style="left:490px;top:670px"></div>
    <div class="brand"><span class="brand-mark"></span><span class="brand-name">bellmere</span></div>
    <h1 class="title">Wash Bag</h1>
    <div class="subtitle">For Delicates</div>
    <p class="tagline">Protects delicate items<br>from tangles and snags<br>in the wash and dryer</p>
  </section>

  <section class="panel panel--back">
    <div class="colour-field"></div>
    <div class="heart-art" role="img" aria-label="Sketched white heart outlines"></div>
    <div class="flower" role="img" aria-label="Violet flower" style="left:492px;top:10px"></div>
    <div class="flower" role="img" aria-label="Violet flower" style="left:8px;top:670px"></div>
    <h2 class="title">Wash Bag</h2>
    <div class="copy">
      <h3>Delicates and hoisery</h3>
      <p>Protects small and delicate items from tangles and snags<br>
      A safe and convenient way to machine wash and dry<br>
      your delicates, such as hosiery, underwear ,<br>
      delicates and baby clothes. They are protected from<br>
      snaring and tangling, even in the largest of loads.</p>
      <h3>Directions.</h3>
      <p>Please observe the garment manufacturers<br>
      care instructions before proceeding.<br>
      Place your delicates inside the bag, fasten<br>
      the zip, and place in the washing machine.<br>
      The fine mesh will allow water and detergent<br>
      to circulate evenly amongst the garments.<br>
      The washbag may be placed directly into<br>
      the clothes dryer if appropriate for your garment.<br>
      The washbag can also be used to protect and isolate<br>
      your delicates in your luggage when travelling.<br>
      Bellmere Products . Vic. 3999.<br>
      Bag made in China, printed and packed in Australia.<br>
      100% polyester</p>
      <p class="spec">30cm x 40cm<br>Freeflow mesh with contrast zip</p>
    </div>
  </section>
</body>
</html>
```